BrightNestle 8.5x11 double-sided stationery design

I need a 8.5x11 double-sided flyer / stationery design for my company BrightNestle. Please follow instructions carefully "Flyer design instructions.pdf" - this is your guide! I have pictures to upload for your use too.

The product is a home decor product which you can mount a photo, then hang it on a wall or put it on a shelf, called "Snap Panel".

Looking for simple, yet effective flyer for sales.

Please return the final flyer in Adobe Illustrator or Photoshop so I can add any final edits, and PDF.
Updates

I would like a sales and marketing FLYER, to promote this product, NOT a stationery design. Sorry about that. Gregor

Target Market(s)

Print shops, event photographers, do-it-your selvers

Industry/Entity Type

Printing

Requirements
Must have
• Must explain the product well, how it's unique, and who might want it. Also, how to get it.

```html
<!DOCTYPE html>
<html lang="en">
<head>
<meta charset="utf-8">
<title>BrightNestle Snap Panel Flyer</title>
<link rel="stylesheet" href="https://fonts.googleapis.com/css2?family=Source+Sans+3:wght@300;400;700&display=swap">
<style>
  :root {
    --wall-light: #eceef0;
    --wall-mid: #d3d6d9;
    --wall-dark: #a9adb2;
    --ink: #3c3c3c;
    --ink-soft: #555a5e;
    --rule: #ffffff;
    --bar-1: #c98a64;
    --bar-2: #a87058;
    --bar-3: #dcc09a;
    --bar-4: #efe0cf;
    --bar-5: #5f5451;
    --wood-dark: #3e2615;
    --wood-mid: #7a4d2d;
    --wood-light: #a87650;
    --band: rgba(30, 22, 16, 0.45);
    --dot: #3fc0f0;
    --white: #ffffff;
    --footer: #1c1c1c;
    --footer-text: #d8d8d8;
  }
  * { margin: 0; padding: 0; box-sizing: border-box; }
  html, body { width: 928px; height: 1200px; overflow: hidden; }
  body { font-family: "Source Sans 3", "Myriad Pro", sans-serif; color: var(--ink); }
  .flyer {
    position: relative; width: 928px; height: 1200px; overflow: hidden;
    background: radial-gradient(ellipse at 50% 30%, var(--wall-light) 0%, var(--wall-mid) 55%, var(--wall-dark) 100%);
  }
  .wood-surface {
    position: absolute; left: 0; top: 690px; width: 928px; height: 389px;
    background: linear-gradient(180deg, var(--wood-dark) 0%, var(--wood-mid) 45%, var(--wood-light) 75%, var(--wood-mid) 100%);
  }
  .swatch-fan {
    position: absolute; left: 200px; top: 49px; width: 168px; height: 168px; border-radius: 50%;
    background: radial-gradient(circle, transparent 0 26%, #e4cfae 27%, #b08462 60%, #6e574d 100%);
  }
  .intro-rule {
    position: absolute; left: 383px; top: 68px; width: 1px; height: 122px; background: var(--rule);
  }
  .intro { position: absolute; left: 396px; top: 73px; width: 420px; }
  .intro-title { font-weight: 400; font-size: 26px; line-height: 26px; color: var(--ink); }
  .intro-text { font-weight: 400; font-size: 20px; line-height: 27px; margin-top: 4px; color: var(--ink); }
  .options { position: absolute; left: 25px; top: 309px; width: 883px; display: flex; }
  .option { flex: 1; text-align: center; }
  .option-bar { height: 17px; }
  .option:nth-child(1) .option-bar { background: var(--bar-1); }
  .option:nth-child(2) .option-bar { background: var(--bar-2); }
  .option:nth-child(3) .option-bar { background: var(--bar-3); }
  .option:nth-child(4) .option-bar { background: var(--bar-4); }
  .option:nth-child(5) .option-bar { background: var(--bar-5); }
  .option-label {
    font-weight: 300; font-size: 20.5px; line-height: 22px; color: var(--ink-soft);
    margin-top: 11px; white-space: nowrap;
  }
  .option:nth-child(4) .option-label { font-size: 18.5px; line-height: 21px; margin-top: 10px; }
  .scene { position: absolute; box-shadow: 0 6px 16px rgba(0,0,0,0.45); }
  .scene-diy { left: 39px; top: 592px; width: 216px; height: 211px;
    background: linear-gradient(135deg, #c9955e 0%, #d9a66c 50%, #b37a48 100%); }
  .scene-event { left: 255px; top: 568px; width: 348px; height: 232px; z-index: 2;
    background: linear-gradient(160deg, #3d6f86 0%, #5f8ea2 40%, #8fa7b6 70%, #2a3a4a 100%); }
  .scene-print { left: 594px; top: 586px; width: 314px; height: 214px;
    background: linear-gradient(170deg, #d8dcdf 0%, #c2c7cb 45%, #9ea4a8 75%, #c06050 100%); }
  .audience-title {
    position: absolute; left: 0; top: 848px; width: 928px; text-align: center;
    font-weight: 300; font-size: 30px; line-height: 36px; color: var(--white);
  }
  .audience-band {
    position: absolute; left: 0; top: 891px; width: 928px; height: 46px; background: var(--band);
    list-style: none; display: flex; justify-content: center; align-items: center; gap: 26px;
  }
  .audience-item { font-weight: 300; font-size: 25px; color: var(--white); display: flex; align-items: center; }
  .audience-item::before {
    content: ""; width: 11px; height: 11px; border-radius: 50%; background: var(--dot); margin-right: 7px;
  }
  .coming-soon { position: absolute; left: 358px; top: 1001px; color: var(--white); line-height: 25px; }
  .coming-soon-title { font-weight: 700; font-size: 24px; letter-spacing: 0.8px; }
  .coming-soon-text { font-weight: 300; font-size: 25px; }
  .site-footer {
    position: absolute; left: 0; top: 1079px; width: 928px; height: 121px; background: var(--footer);
  }
  .buy { position: absolute; left: 29px; top: 28px; color: var(--white); }
  .buy-title { font-weight: 700; font-size: 30px; line-height: 32px; }
  .buy-text { font-weight: 300; font-size: 25px; line-height: 26px; }
  .contact { position: absolute; left: 626px; top: 14px; list-style: none; color: var(--footer-text); }
  .contact li { font-weight: 400; font-size: 19px; line-height: 29px; }
</style>
</head>
<body>
<main class="flyer">
  <div class="wood-surface" role="img" aria-label="Polished wooden tabletop surface"></div>

  <div class="swatch-fan" role="img" aria-label="Fan of wood-tone edge trim swatches"></div>
  <div class="intro-rule"></div>
  <section class="intro">
    <h1 class="intro-title">Don’t like the standard black<br>edge or somethine else?</h1>
    <p class="intro-text">We can customize any of the following<br>to make the perfect boards for you.</p>
  </section>

  <section class="options">
    <div class="option"><div class="option-bar"></div><p class="option-label">Edge trim<br>color or texture</p></div>
    <div class="option"><div class="option-bar"></div><p class="option-label">Thickness, from<br>0.25” to 3 inches</p></div>
    <div class="option"><div class="option-bar"></div><p class="option-label">Size, from 4x4” to<br>20x30” and higher</p></div>
    <div class="option"><div class="option-bar"></div><p class="option-label">Backside configuration<br>for special mounting<br>techniques</p></div>
    <div class="option"><div class="option-bar"></div><p class="option-label">Directprint Snap<br>Panel (for UV<br>printers or similar)</p></div>
  </section>

  <div class="scene scene-diy" role="img" aria-label="Do-it-yourself workbench with wood samples, paint roller and brushes"></div>
  <div class="scene scene-event" role="img" aria-label="Event photographer shooting a wedding couple"></div>
  <div class="scene scene-print" role="img" aria-label="Print shop worker operating a printer"></div>

  <h2 class="audience-title">Perfect For:</h2>
  <ul class="audience-band">
    <li class="audience-item">Doityourselfers</li>
    <li class="audience-item">Event photographers</li>
    <li class="audience-item">Print shops, big or small</li>
  </ul>

  <section class="coming-soon">
    <p class="coming-soon-title">Coming soon&nbsp; website for consumers:</p>
    <p class="coming-soon-text">upload your photos, and finished boards sent back</p>
  </section>

  <footer class="site-footer">
    <div class="buy">
      <p class="buy-title">Where to buy?</p>
      <p class="buy-text">Unprinted / mountready.</p>
    </div>
    <ul class="contact">
      <li>www.brightpanelhome.com</li>
      <li>18005550142</li>
      <li>admin@brightpanelhome.com</li>
    </ul>
  </footer>
</main>
</body>
</html>
```